Creative, fun banner ads needed for tropical shaved ice company

Create assorted, most popular-sized banner ads for shaved ice company> Logo files attached. Looking for eye-catching, fun ads that would make any parent of a child 2-17 years old want to click the ad and have us to be a part of the festivities so they can enjoy our tropical-flavored shaved ice; to hire us for a party or community event or fund-raiser.

Target Market(s)

parents with children between 2 - 18 years of age; charities, fund-raisers, event planners. think about the websites/CL pages where this ad will most like appear.

Font styles to use
Sans Serif

Requirements
Must have
• 1. logo
2. must be editable so I can reuse for different themes (birthdays, major holidays, special events, charity events)
3. colorful or otherwise eye-catching/appealing.
4. keep with the logo theme OR use logo and have different, yet fun, happy theme
5. otherwise simple, clean, pleasant design that illicits a fun, happy image
6. just keep in mind that shaved ice is delicious, fun, and beats the scorching sun here in South Florida. https://palmcovesnowcones.com or https://chatterlink.com/palmcovesnowcones
Nice to have
• reuse iguana character somehow; possibly holding a shaved ice
lighthouse
Should not have
• dark or gloomy colors/themes
too much stuff; too much clutter.

```html
<!DOCTYPE html>
<html lang="en">
<head>
<meta charset="utf-8">
<title>Palm Cove Snow Cones – Perfectly shaved banner</title>
<link rel="stylesheet" href="https://fonts.googleapis.com/css2?family=Baloo+2:wght@700&family=Cabin+Condensed:wght@500&display=swap">
<style>
  :root {
    --stage: #141414;
    --red: #ee1c1c;
    --red-deep: #c9100f;
    --red-light: #ff3a2a;
    --yellow: #ffe100;
    --sun: #fcd21a;
    --sun-deep: #f6b817;
    --white: #ffffff;
    --cup: #fbb33a;
    --brand-dot: #2cb5e8;
  }
  * { margin: 0; padding: 0; box-sizing: border-box; }
  html, body {
    width: 1200px; height: 720px; overflow: hidden;
    background: var(--stage);
  }
  .banner {
    position: absolute; left: 40px; top: 67px;
    width: 1120px; height: 586px; overflow: hidden;
    background: var(--red);
  }
  .banner__backdrop {
    position: absolute; inset: 0;
    background:
      radial-gradient(ellipse at 25% 45%, var(--red-deep) 0%, transparent 55%),
      linear-gradient(110deg, var(--red) 0%, var(--red-light) 50%, var(--red) 100%);
  }
  .banner__shapes { position: absolute; inset: 0; }

  .brand {
    position: absolute; left: 82px; top: 52px;
    display: flex; align-items: center; gap: 14px;
    font-family: "Baloo 2", sans-serif; font-weight: 700;
    font-size: 40px; line-height: 0.95; color: var(--yellow);
  }
  .brand__dot {
    flex: none; width: 72px; height: 72px; border-radius: 50%;
    background: var(--brand-dot);
  }

  .headline {
    position: absolute; left: 93px; top: 228px;
    font-family: "Baloo 2", sans-serif; font-weight: 700;
    font-size: 58px; line-height: 1; color: var(--yellow);
    transform: rotate(1.5deg); transform-origin: left center;
    white-space: nowrap;
  }
  .headline__swoosh { position: absolute; left: 66px; top: 292px; }
  .intro {
    position: absolute; left: 98px; top: 322px;
    font-family: "Cabin Condensed", sans-serif; font-weight: 500;
    font-size: 17px; line-height: 22px; color: var(--white);
    white-space: nowrap;
  }

  .art { position: absolute; }
  .art--cups {
    left: 14px; top: 381px; width: 310px; height: 205px;
    background: linear-gradient(180deg, var(--cup), #f7a12c);
    opacity: .85; border-radius: 40px 40px 0 0;
  }
  .art--collage {
    left: 358px; top: 412px; width: 252px; height: 174px;
    background: linear-gradient(135deg, #e9e3d8, #f3a540 55%, #b9343c);
    transform: rotate(-4deg); border: 4px solid var(--white);
  }
  .art--berry-glass {
    left: 768px; top: 140px; width: 160px; height: 358px;
    border-radius: 50% 50% 10px 10px / 22% 22% 10px 10px;
    background: linear-gradient(180deg, #d98fb4 0%, #a8456f 45%, #7d1f3d 100%);
  }
  .art--strawberry-glass {
    left: 872px; top: 122px; width: 208px; height: 402px;
    border-radius: 50% 50% 40% 40% / 24% 24% 10% 10%;
    background: linear-gradient(180deg, #e0444a 0%, #f6b7c3 28%, #f3c5cd 55%, #e9e9ee 80%, #d7d7dc 100%);
  }
  .art--rainbow-cone {
    left: 602px; top: 190px; width: 220px; height: 330px;
    border-radius: 50% 50% 30% 30% / 34% 34% 12% 12%;
    background: linear-gradient(100deg, #4fb8e4 0%, #9fd88a 30%, #f3e35a 55%, #f07a4c 80%, #e8403c 100%);
  }
</style>
</head>
<body>
  <main class="banner">
    <div class="banner__backdrop" role="img" aria-label="Photo of fresh strawberries on a red checked cloth"></div>

    <svg class="banner__shapes" width="1120" height="586" viewBox="0 0 1120 586" aria-hidden="true">
      <path d="M545 0 C600 70 700 120 790 115 C850 112 880 50 940 55 C1010 60 1060 160 1120 205 L1120 0 Z" fill="var(--sun)"/>
      <path d="M545 0 C600 70 700 120 790 115 C850 112 880 50 940 55 C1010 60 1060 160 1120 205" fill="none" stroke="var(--white)" stroke-width="9"/>
      <path d="M560 0 C620 60 710 100 795 98 C860 96 885 38 945 42 C1010 46 1065 140 1120 185" fill="none" stroke="var(--white)" stroke-width="2"/>
      <path d="M618 586 C605 540 620 495 665 480 C760 450 860 520 960 450 C1030 400 1080 345 1120 340 L1120 586 Z" fill="var(--sun-deep)"/>
      <path d="M618 586 C605 540 620 495 665 480 C760 450 860 520 960 450 C1030 400 1080 345 1120 340" fill="none" stroke="var(--white)" stroke-width="8"/>
      <path d="M640 586 C630 545 645 510 690 500 C780 480 870 535 970 470 C1040 420 1085 370 1120 362" fill="none" stroke="var(--white)" stroke-width="2"/>
    </svg>

    <div class="brand"><span class="brand__dot"></span><span>Palm Cove<br>Snow Cones</span></div>

    <h1 class="headline">Perfectly shaved..</h1>
    <svg class="headline__swoosh" width="490" height="26" viewBox="0 0 490 26" aria-hidden="true">
      <path d="M2 22 C150 2 340 2 488 20 C340 8 150 10 2 22 Z" fill="var(--yellow)" stroke="var(--yellow)" stroke-width="3" stroke-linejoin="round"/>
    </svg>
    <p class="intro">Our best-in-class shaved ice starts with the best clear<br>block ice avialble that is perfectly shaved...</p>

    <div class="art art--cups" role="img" aria-label="Illustration of three frozen drink cups with straws"></div>
    <div class="art art--collage" role="img" aria-label="Collage of photos showing shaved ice, oranges and fruit drinks"></div>
    <div class="art art--berry-glass" role="img" aria-label="Photo of berry shaved ice in a tall glass"></div>
    <div class="art art--strawberry-glass" role="img" aria-label="Photo of strawberry shaved ice layered in a stemmed glass"></div>
    <div class="art art--rainbow-cone" role="img" aria-label="Photo of a rainbow snow cone in a blue cone cup"></div>
  </main>
</body>
</html>
```